Game, Voice & Dedicated Server Company Needs a Business Card Design

We need a new business card design, centered around our new logo (PSD provided below).

Designs that we do like:
https://pixelmarsh.net/item/corporate-business-card/5382017?s_rank=43 (needs to be made more eye catching)

Our main areas of business are:
- Dedicated Servers
- Game Servers
- Voice Servers
- Mitigation Security Specialists

Industry/Entity Type

Business

Contact Information for Business Card

On the card: (and anything else you would suggest)
- Staff member name
- Staff member position in company
- Staff member phone number
- Staff member email
- Other / Staff member Skype
- Website link

Colors
9bcb3c
abd036

Requirements
Must have
• Design of Card:
• - Green (same green as the logo)
• - Business / Corporate design
• - Something a little different / abstract that shouts premium

```html
<!DOCTYPE html>
<html lang="en">
<head>
<meta charset="utf-8">
<title>Corvane Hosting – Business Card</title>
<link href="https://fonts.googleapis.com/css2?family=Arimo:wght@400;700&family=Open+Sans:wght@400;600&display=swap" rel="stylesheet">
<style>
  :root {
    --backdrop: #3b3430;
    --card: #1c1c1d;
    --card-edge: #2a2a2b;
    --green: #9bcb3c;
    --green-light: #abd036;
    --white: #f2f2f2;
    --grey: #8e8e8e;
    --divider: #555556;
  }
  * { box-sizing: border-box; margin: 0; padding: 0; }
  html, body {
    width: 1200px;
    height: 787px;
    overflow: hidden;
    background: var(--backdrop);
  }
  .stage {
    position: relative;
    width: 1200px;
    height: 787px;
  }
  .card {
    position: absolute;
    top: 238px;
    width: 540px;
    height: 310px;
    background: var(--card);
    border: 1px solid var(--card-edge);
    box-shadow: 0 10px 28px rgba(0,0,0,.45);
    color: var(--white);
    font-family: "Arimo", Arial, sans-serif;
  }
  .card--front { left: 40px; }
  .card--back  { left: 620px; }

  /* Brand name */
  .brand {
    display: flex;
    align-items: center;
    gap: 12px;
  }
  .brand__mark {
    width: 34px;
    height: 34px;
    background: var(--green);
    flex: none;
  }
  .brand__name {
    font-family: "Arimo", Arial, sans-serif;
    font-weight: 700;
    color: var(--green);
    line-height: .95;
    letter-spacing: -.5px;
    text-transform: uppercase;
  }

  /* Front */
  .card--front .brand {
    position: absolute;
    left: 52px;
    top: 58px;
  }
  .card--front .brand__mark { width: 44px; height: 44px; }
  .card--front .brand__name { font-size: 34px; }
  .services {
    position: absolute;
    left: 52px;
    bottom: 56px;
    list-style: none;
    font-size: 15px;
    line-height: 1.55;
    color: var(--white);
  }
  .services__dot {
    display: inline-block;
    width: 6px;
    height: 6px;
    border-radius: 50%;
    background: var(--green);
    margin: 0 6px 2px;
    vertical-align: middle;
  }

  /* Back */
  .card--back .brand {
    position: absolute;
    left: 36px;
    top: 112px;
  }
  .card--back .brand__name { font-size: 24px; }
  .divider {
    position: absolute;
    left: 286px;
    top: 64px;
    width: 1px;
    height: 182px;
    background: linear-gradient(to bottom, transparent, var(--divider) 20%, var(--divider) 80%, transparent);
  }
  .contact {
    position: absolute;
    left: 306px;
    top: 70px;
    font-family: "Open Sans", Arial, sans-serif;
  }
  .contact__name {
    font-size: 20px;
    font-weight: 600;
    color: var(--green-light);
  }
  .contact__role {
    font-size: 13px;
    color: var(--grey);
    margin-bottom: 12px;
  }
  .contact__list { list-style: none; }
  .contact__item {
    display: flex;
    align-items: center;
    gap: 8px;
    font-size: 14px;
    line-height: 1.7;
    color: var(--white);
  }
  .contact__icon {
    width: 14px;
    height: 14px;
    flex: none;
    fill: var(--green);
  }
</style>
</head>
<body>
<main class="stage">

  <section class="card card--front" aria-label="Business card front">
    <div class="brand">
      <span class="brand__mark"></span>
      <span class="brand__name">Corvane<br>Hosting</span>
    </div>
    <ul class="services">
      <li>Dedicated Servers<span class="services__dot"></span>Game Servers</li>
      <li>Voice Servers<span class="services__dot"></span>Business relations</li>
    </ul>
  </section>

  <section class="card card--back" aria-label="Business card back">
    <div class="brand">
      <span class="brand__mark"></span>
      <span class="brand__name">Corvane<br>Hosting</span>
    </div>
    <span class="divider"></span>
    <div class="contact">
      <p class="contact__name">Daniel Reyes</p>
      <p class="contact__role">CEO/Founder</p>
      <ul class="contact__list">
        <li class="contact__item">
          <svg class="contact__icon" viewBox="0 0 16 16" aria-hidden="true"><path d="M3 1h3l1.5 3.5-2 1.3a9 9 0 0 0 4.7 4.7l1.3-2L15 10v3a2 2 0 0 1-2 2A12 12 0 0 1 1 3a2 2 0 0 1 2-2z"/></svg>
          555 014 2290
        </li>
        <li class="contact__item">
          <svg class="contact__icon" viewBox="0 0 16 16" aria-hidden="true"><path d="M1 3h14v10H1z M1 3l7 6 7-6" fill="var(--green)"/><path d="M1.5 3.5 8 9l6.5-5.5" fill="none" stroke="#1c1c1d" stroke-width="1.3"/></svg>
          name@corvanehost.com
        </li>
        <li class="contact__item">
          <svg class="contact__icon" viewBox="0 0 16 16" aria-hidden="true"><circle cx="8" cy="8" r="7"/><path d="M1 8h14M8 1c-3 3.5-3 10.5 0 14M8 1c3 3.5 3 10.5 0 14" fill="none" stroke="#1c1c1d" stroke-width="1.1"/></svg>
          www.corvanehost.com
        </li>
        <li class="contact__item">
          <svg class="contact__icon" viewBox="0 0 16 16" aria-hidden="true"><circle cx="8" cy="8" r="7"/></svg>
          corvanehost.com
        </li>
      </ul>
    </div>
  </section>

</main>
</body>
</html>
```